Chatterbox and Pictoria advertisment

We need Chatterbox and Pictoria ads.  Simple ad with Alaska themed background.
This ad is to introduce our new KORVO Internet service.
--Speeds to 500 mbps
-- Packages start at only $89.99 for speeds to 100mbps
-- Fiber Optic based connection, Not satellite
-- Extreme low latency, consistent speeds
--FREE equipment, FREE Installation, FREE wifi router, First month of service FREE

This is for a Chatterbox/Pictoria ad. We already have a logo

```html
<!DOCTYPE html>
<html lang="en">
<head>
<meta charset="utf-8">
<title>KORVO Internet – Northwind Relay</title>
<link rel="stylesheet" href="https://fonts.googleapis.com/css2?family=Anton&family=Barlow+Condensed:ital,wght@1,500;1,700&family=Inter:wght@300;400;600;700;800&display=swap">
<style>
  :root {
    --aurora-green: #5fd16a;
    --aurora-light: #d9f2b8;
    --aurora-magenta: #b0477f;
    --sky-dark: #143a2e;
    --snow: #dfe8e6;
    --forest: #1d2f2c;
    --text-light: #ffffff;
    --text-dark: #0e0e0e;
  }
  * { margin: 0; padding: 0; box-sizing: border-box; }
  html, body { width: 1200px; height: 1200px; overflow: hidden; background: #fff; }
  .ad {
    position: relative;
    width: 1200px;
    height: 1200px;
    overflow: hidden;
    font-family: "Inter", sans-serif;
    color: var(--text-light);
  }
  .ad-backdrop {
    position: absolute; inset: 0;
    background:
      radial-gradient(ellipse 55% 40% at 85% 18%, rgba(176,71,127,0.9), transparent 70%),
      radial-gradient(ellipse 70% 35% at 60% 38%, rgba(217,242,184,0.85), transparent 70%),
      radial-gradient(ellipse 60% 45% at 25% 22%, rgba(95,209,106,0.85), transparent 70%),
      linear-gradient(180deg, var(--sky-dark) 0%, #2f6a4a 30%, #6f9a86 46%, #4d5f5c 62%, var(--forest) 78%, var(--snow) 100%);
  }
  .headline {
    position: absolute;
    left: 103px; top: 100px;
    font-family: "Barlow Condensed", sans-serif;
    font-style: italic;
    font-weight: 500;
    font-size: 100px;
    line-height: 1;
    letter-spacing: 1px;
  }
  .headline strong { font-weight: 700; }
  .free-block {
    position: absolute;
    left: 106px; top: 262px;
    display: flex; align-items: center; gap: 26px;
  }
  .free-word {
    font-family: "Anton", sans-serif;
    font-size: 238px;
    line-height: 0.8;
    color: var(--text-dark);
    letter-spacing: -2px;
  }
  .free-list {
    list-style: none;
    font-weight: 600;
    font-size: 38px;
    line-height: 49px;
    color: var(--text-dark);
  }
  .pricing {
    position: absolute;
    left: 109px; top: 552px;
  }
  .pricing-intro { font-weight: 300; font-size: 36px; line-height: 1; }
  .pricing-amount {
    font-weight: 800; font-size: 148px; line-height: 1;
    letter-spacing: -3px; margin: 6px 0 10px -4px;
  }
  .feature-list { list-style: none; font-weight: 300; font-size: 34px; line-height: 52px; }
  .feature-list strong { font-weight: 700; }
  .product-name {
    position: absolute;
    left: 104px; top: 955px;
    font-weight: 700; font-size: 158px; line-height: 1;
    letter-spacing: 2px;
  }
  .provider {
    position: absolute;
    right: 98px; top: 1045px;
    display: flex; align-items: center; gap: 16px;
    font-weight: 600; font-size: 52px; line-height: 1;
  }
  .provider-dot { width: 26px; height: 26px; border-radius: 50%; background: var(--text-light); }
</style>
</head>
<body>
<main class="ad">
  <div class="ad-backdrop" role="img" aria-label="Green and magenta northern lights over snow-covered Alaskan mountains and a spruce forest"></div>

  <h1 class="headline">SPEEDS UP TO <strong>500 MBPS!</strong></h1>

  <section class="free-block">
    <div class="free-word">FREE</div>
    <ul class="free-list">
      <li>EQUIPMENT</li>
      <li>INSTALLATION</li>
      <li>WIFI ROUTER</li>
      <li>1ST MONTH OF SERVICE</li>
    </ul>
  </section>

  <section class="pricing">
    <p class="pricing-intro">PACKAGES START AT ONLY</p>
    <p class="pricing-amount">$89.99</p>
    <ul class="feature-list">
      <li>FOR SPEEDS TO <strong>100MBPS</strong></li>
      <li><strong>FIBER OPTIC</strong> BASED CONNECTION, NOT SATELLITE</li>
      <li>EXTREME LOW LATENCY, CONSISTENT SPEEDS</li>
    </ul>
  </section>

  <div class="product-name">KORVO</div>

  <div class="provider">
    <span class="provider-dot"></span>
    <span class="provider-name">Northwind Relay</span>
  </div>
</main>
</body>
</html>
```